K7 Teaser

One page teaser for our business information and model. A financial service SPV platform.

Target Market(s)

Financial Professionals

Industry/Entity Type

Financial Service

Font styles to use
Sans Serif

Colors
ffcf3e
ffffff
cfcfcf
9d9d9d
aaaaaa
fbed22
ffc214
fee18a
fbee3f

Requirements
Must have
• Unique appearance of USPs.
• Important claims: Low Cost. First Class.
• and: We liberate the buy-side from the sell-side
Nice to have
• maybe keyword cloud

```html
<!DOCTYPE html>
<html lang="en">
<head>
<meta charset="utf-8">
<title>K7 Teaser</title>
<link href="https://fonts.googleapis.com/css2?family=Lato:wght@300;400;700&family=Play:wght@400;700&display=swap" rel="stylesheet">
<style>
  :root {
    --gold: #e1a82a;
    --gold-light: #ffcf3e;
    --ink: #1a1a1a;
    --panel: #161616;
    --white: #ffffff;
    --grey-text: #6e6e6e;
    --grey-bar: #4a4a4a;
    --silver: #cfcfcf;
  }
  * { box-sizing: border-box; margin: 0; padding: 0; }
  html, body { width: 888px; height: 1200px; overflow: hidden; background: var(--white); }
  body { font-family: "Lato", sans-serif; color: var(--ink); }
  .teaser { position: relative; width: 888px; height: 1200px; background: var(--white); overflow: hidden; }

  .hero { position: absolute; left: 0; top: 0; width: 888px; height: 410px; }
  .hero-art { position: absolute; left: 0; top: 0; }
  .hero-claims { position: absolute; left: 326px; top: 88px; color: var(--white); font-weight: 400; }
  .claim-main { font-size: 43px; line-height: 48px; letter-spacing: 0.5px; }
  .claim-sub { font-size: 31px; line-height: 36px; color: var(--gold-light); font-weight: 300; }
  .claim-sub strong { font-weight: 700; }
  .claim-tail { font-size: 37px; line-height: 44px; }

  .brand-row { position: absolute; top: 418px; left: 72px; right: 40px; height: 80px; display: flex; align-items: center; }
  .brand { display: flex; align-items: center; gap: 14px; width: 300px; }
  .brand-dot { width: 52px; height: 52px; border-radius: 50%; background: var(--gold); }
  .brand-name { font-size: 38px; font-weight: 300; color: var(--gold); letter-spacing: 2px; border-left: 1px solid var(--gold); padding-left: 14px; }
  .liberate { font-family: "Play", sans-serif; font-size: 31px; line-height: 40px; font-weight: 400; color: var(--ink); margin-left: 2px; }

  .intro { position: absolute; top: 518px; left: 60px; width: 800px; font-size: 12.6px; line-height: 14.6px; color: var(--grey-text); }

  .offer-panel { position: absolute; top: 651px; left: 0; width: 888px; height: 374px; background: var(--panel); color: var(--white); padding: 30px 0 0 75px; }
  .panel-heading { display: inline-block; font-size: 19px; font-weight: 300; color: var(--gold); border-bottom: 1px solid var(--gold); padding-bottom: 2px; letter-spacing: 0.3px; }
  .usp-label { font-size: 15px; font-weight: 700; margin-top: 2px; }
  .bullet-cols { display: flex; margin-top: 16px; }
  .bullet-cols ul { list-style: none; font-size: 13.2px; line-height: 17.5px; }
  .bullet-cols li::before { content: "•"; margin-right: 10px; }
  .col-a { width: 285px; }
  .col-b { width: 252px; }
  .grow { margin-top: 42px; }
  .grow .bullet-cols { margin-top: 20px; }
  .grow .col-b { width: 272px; }

  .pricing-band { position: absolute; top: 1028px; left: 0; width: 888px; height: 52px; background: var(--gold); display: flex; align-items: center; padding-left: 60px; font-size: 13.5px; color: var(--ink); }
  .pricing-band span::before { content: "•"; margin-right: 8px; }
  .price-a { width: 265px; }
  .price-b { width: 354px; }

  .about { position: absolute; top: 1106px; left: 60px; width: 800px; font-size: 11.2px; line-height: 14px; color: #333; }

  .contact-bar { position: absolute; left: 0; bottom: 0; width: 888px; height: 42px; background: var(--grey-bar); color: var(--white); font-size: 13px; display: flex; align-items: center; justify-content: center; }
</style>
</head>
<body>
<main class="teaser">
  <header class="hero">
    <svg class="hero-art" width="888" height="410" viewBox="0 0 888 410">
      <defs>
        <radialGradient id="stairwell" cx="0.22" cy="0.35" r="0.9">
          <stop offset="0" stop-color="#6b5a3c"/>
          <stop offset="0.35" stop-color="#2e2a24"/>
          <stop offset="1" stop-color="#0d0d0d"/>
        </radialGradient>
      </defs>
      <path role="img" aria-label="Photo looking up a dark square stairwell" fill="url(#stairwell)"
            d="M0,0 H888 V262 C600,270 400,300 267,330 C180,300 80,275 0,258 Z"/>
      <path fill="var(--gold)"
            d="M0,258 C80,275 180,300 267,330 C400,300 600,270 888,262 V282 C650,288 400,330 267,402 C200,360 120,300 0,272 Z"/>
    </svg>
    <div class="hero-claims">
      <p class="claim-main">LOW COST. FIRST CLASS</p>
      <p class="claim-sub"><strong>We democratise</strong> structured financial</p>
      <p class="claim-tail">PRODUCT ISSUANCE</p>
    </div>
  </header>

  <section class="brand-row">
    <div class="brand">
      <span class="brand-dot"></span>
      <span class="brand-name">K7</span>
    </div>
    <h1 class="liberate">WE LIBERATE THE BUY-SIDE<br>FROM THE SELL-SIDE</h1>
  </section>

  <p class="intro">We serve our clients with the power to create their own branded, tailor-made financial products and investment solutions by providing them with right tools and structures to establish and operate first class off-balance sheet issuance vehicles (SPV). We create unique solutions to expand your business reach, services and qualities by liberating financial product issuance to buy-side. Asset owners, distributors and managers are given the full capability to securitise their own asset base in unlimited capacity, outside their balance sheet with customisable transparency and counterparty risk. A clear and simple solutions to serve your best interests and without the need for conventional sell-side issuers.</p>

  <section class="offer-panel">
    <div class="usps">
      <h2 class="panel-heading">YOUR BRAND. YOUR REWARD. YOUR SOLUTION.</h2>
      <p class="usp-label">USPs</p>
      <div class="bullet-cols">
        <ul class="col-a">
          <li>Off-balance sheet</li>
          <li>Own issuance vehicle (SPV)</li>
          <li>Regulatory compliant (MIFID)</li>
          <li>Swiss Paying Agent</li>
          <li>Various off-shore locations</li>
        </ul>
        <ul class="col-b">
          <li>Open Architecture</li>
          <li>Daily Liquidity</li>
          <li>Quick setup</li>
          <li>Transparent secondary market</li>
          <li>Full transparent pricing</li>
        </ul>
        <ul class="col-c">
          <li>Customised Transparency</li>
          <li>Low cost structure</li>
          <li>Your own fee policy</li>
          <li>Investment &amp; risk control</li>
        </ul>
      </div>
    </div>
    <div class="grow">
      <h2 class="panel-heading">GROW YOUR BUSINESS. OFFER YOUR PRODUCTS:</h2>
      <div class="bullet-cols">
        <ul class="col-a">
          <li>Structured Products</li>
          <li>Active Managed Certificate (AMC)</li>
          <li>Static Trackers</li>
          <li>Securitisation of depth</li>
          <li>Crypto-backed securities</li>
        </ul>
        <ul class="col-b">
          <li>Privat Equity Finance</li>
          <li>Insurance Linked Securities</li>
          <li>Leverage Products</li>
        </ul>
        <ul class="col-c">
          <li>Trade Financial</li>
          <li>Asset backed Sec.</li>
        </ul>
      </div>
    </div>
  </section>

  <section class="pricing-band">
    <span class="price-a">Establishment Cost CHF 20'000</span>
    <span class="price-b">Recurring Cost Yearly 20 BPS (&gt; CHF 20'000)</span>
    <span class="price-c">Product Cost CHF 2'000</span>
  </section>

  <p class="about">K7 Financial Product AG is a financial service provider built on the unique experience and robust track record of its team. Our founders gathered the most qualified experts to benefit our clients and business partners.</p>

  <footer class="contact-bar">K7 Financial Products AG I Lindenplatz 14 I CH-8002 Zürich I www.k7-platform.example I +41 44 000 12 34</footer>
</main>
</body>
</html>
```